New Business Card Design Project

We are looking for a talented individual to create a truly awesome/unique business card design for us. We are looking for a someone to design something that will really stand out from the crowd - we don't mind what ideas you come up with (ie embossed/flat/matte/shine etc etc) just wow us with your creativity.
Updates

Target Market(s)

Video Games Industry Professionals (all levels of seniority from QA Testers through to CEOs)

Contact Information for Business Card

Company logo (see upload)
Company name: Northbay Play Careers Ltd
Employee Name: Darren Elsby
Job title: CEO
Website: www.nbpc2go.example
Office +44 1632 960418
Mobile: +44 7700 900276
Email: darren@nbpc2go.example

Colors

Designer to choose colors to be used in the design.

Requirements
Must have
• The business card design MUST contain all the information listed in the BUSINESS CARD DETAILS box.
• You will see the colours that are relevant to us (ie company logo) in the uploaded imagery - however you do not have to use all these colours when designing the business card itself
• MUST BE DOUBLE SIDED

```html
<!DOCTYPE html>
<html lang="en">
<head>
<meta charset="utf-8">
<title>Northbay Play Careers – Business Card</title>
<link href="https://fonts.googleapis.com/css2?family=Montserrat:wght@600;700&family=Open+Sans:wght@400;600&display=swap" rel="stylesheet">
<style>
  :root {
    --backdrop: #2b2b2b;
    --navy: #1c2c5e;
    --orange: #f47b20;
    --paper: #ffffff;
    --ink: #2a2a2a;
    --rule: #3a3a3a;
  }
  * { box-sizing: border-box; margin: 0; padding: 0; }
  html, body { width: 1200px; height: 895px; overflow: hidden; }
  body {
    background: var(--backdrop);
    font-family: "Open Sans", sans-serif;
    position: relative;
  }
  .card {
    position: absolute;
    width: 620px;
    height: 354px;
    box-shadow: 0 12px 30px rgba(0,0,0,0.5);
    overflow: hidden;
  }
  .card--front { left: 110px; top: 60px; background: var(--navy); }
  .card--back  { left: 470px; top: 480px; background: var(--paper); }

  .brand {
    position: absolute;
    display: flex;
    align-items: center;
    gap: 16px;
    font-family: "Montserrat", sans-serif;
    font-weight: 700;
    line-height: 1.05;
  }
  .brand__dot { border-radius: 50%; flex: none; }
  .card--front .brand { left: 120px; top: 128px; color: var(--paper); font-size: 38px; }
  .card--front .brand__dot { width: 90px; height: 90px; background: var(--paper); }
  .card--back .brand { right: 40px; top: 40px; color: var(--navy); font-size: 26px; }
  .card--back .brand__dot { width: 62px; height: 62px; background: var(--navy); }

  .divider {
    position: absolute;
    left: 190px; right: 40px; top: 130px;
    height: 1px; background: var(--rule);
  }
  .website {
    position: absolute;
    right: 30px; top: 165px;
    font-size: 13px; color: var(--ink);
  }
  .website-bar {
    position: absolute;
    right: 0; top: 190px;
    width: 120px; height: 8px; background: var(--orange);
  }
  .person { position: absolute; left: 34px; top: 196px; }
  .person__name {
    font-family: "Montserrat", sans-serif;
    font-weight: 700; font-size: 22px; color: var(--navy);
    letter-spacing: 0.5px;
  }
  .person__sep { color: var(--ink); font-weight: 400; margin: 0 6px; }
  .person__role { color: var(--orange); font-size: 15px; font-weight: 600; }
  .person__company { font-size: 14px; color: var(--ink); margin-top: 2px; }
  .person__rule { width: 200px; height: 1px; background: var(--rule); margin: 10px 0 8px; }
  .contact { list-style: none; font-size: 15px; color: var(--ink); }
  .contact li { display: flex; align-items: center; gap: 12px; height: 22px; }
  .contact svg { width: 14px; height: 14px; fill: none; stroke: var(--orange); stroke-width: 2; }
  .contact .icon-fill { fill: var(--orange); stroke: none; }
</style>
</head>
<body>
  <section class="card card--front" aria-label="Card front">
    <div class="brand"><span class="brand__dot"></span><span>Northbay Play<br>Careers</span></div>
  </section>

  <section class="card card--back" aria-label="Card back">
    <div class="brand"><span class="brand__dot"></span><span>Northbay Play<br>Careers</span></div>
    <div class="divider"></div>
    <p class="website">www.nbpc2go.example</p>
    <div class="website-bar"></div>

    <div class="person">
      <p class="person__name">DARREN ELSBY<span class="person__sep">|</span><span class="person__role">CEO</span></p>
      <p class="person__company">Northbay Play Careers Ltd</p>
      <div class="person__rule"></div>
      <ul class="contact">
        <li><svg viewBox="0 0 14 14"><rect x="3" y="1" width="8" height="12" rx="1.5"/></svg>+44 7700 900276</li>
        <li><svg viewBox="0 0 14 14"><path class="icon-fill" d="M2 1h3l1 3-2 1.5a8 8 0 0 0 4.5 4.5L10 8l3 1v3c0 1-1 1.5-1.5 1.5A11 11 0 0 1 .5 2.5C.5 2 1 1 2 1z"/></svg>+44 1632 960418</li>
        <li><svg viewBox="0 0 14 14"><path class="icon-fill" d="M1 3h12v8H1z"/><path d="M1 3l6 5 6-5" stroke="#fff" stroke-width="1.2"/></svg>darren@nbpc2go.example</li>
      </ul>
    </div>
  </section>
</body>
</html>
```